Web hosting company, 10th year anniversary needs appropriate graphic

We need luxury design (black background with gold elements, etc.) to celebrate 10th year company anniversary, accompanied by appropriate graphics that will be used on various things, like fb, web, print.
We need graphic design (with source .psd) for
- Facebook cover
- Our web site cover (www.brindlecove.com)
- T-shirt print (on white and dark blue t-shirts)
- Coffee mug print (white mug)
Attached is our current design (blue/white with mascot)
Logo font is Tele-Marines (tele2) and other text is Open Sans Light.
Text on the final graphic will be in Croatian language.
It Company
- Tele-Marines, Open Sans Light

```html
<!DOCTYPE html>
<html lang="en">
<head>
<meta charset="utf-8">
<title>Brindlecove – 10th Anniversary Banners</title>
<link href="https://fonts.googleapis.com/css2?family=Open+Sans:wght@300;400;600&display=swap" rel="stylesheet">
<style>
  :root{
    --page:#ffffff;
    --black:#0b0b0c;
    --panel:#141416;
    --panel-pattern:#1f1f22;
    --text-grey:#d9d9d9;
    --teal:#3fb3c8;
    --blue:#4a9fe0;
    --gold:#d7b24a;
    --gold-light:#f3dc8a;
    --gold-dark:#8d6a1c;
    --red:#b3181d;
    --silver:#c9ccd1;
  }
  *{box-sizing:border-box;margin:0;padding:0}
  html,body{width:776px;height:1200px;overflow:hidden;background:var(--page)}
  body{font-family:"Open Sans",Arial,sans-serif;font-weight:300;position:relative}
  .banner{position:absolute;left:13px;width:750px;height:270px;background:var(--black);overflow:hidden}
  .banner--ribbon{top:12px}
  .banner--sparkle{top:310px}
  .banner--badge{top:608px}
  .banner--gold-bow{top:906px}
  .mascot-panel{position:absolute;right:0;top:0;width:290px;height:100%;
    background:radial-gradient(circle at 50% 45%,var(--panel-pattern),var(--panel) 70%)}
  .mascot{position:absolute;right:40px;top:22px;width:200px;height:226px;border-radius:46% 46% 30% 30%;
    background:radial-gradient(circle at 40% 35%,#f2f3f5,var(--silver) 45%,#6d7178 100%)}
  .headline{position:absolute;color:var(--text-grey);font-size:34px;line-height:1.3}
  .headline em{font-style:normal;color:var(--teal);font-weight:400}
  .brand{position:absolute;right:28px;bottom:18px;color:#fff;font-size:22px;font-weight:600;letter-spacing:2px}
  /* banner 1 */
  .banner--ribbon .headline{left:34px;top:26px}
  .silk-ribbon{position:absolute;left:0;top:150px;width:460px;height:56px;
    background:linear-gradient(180deg,#0e0e0e,#3a3a3c 45%,#0e0e0e)}
  /* banner 2 */
  .sparkle-waves{position:absolute;left:0;top:0;width:470px;height:100%;
    background:radial-gradient(ellipse at 40% 45%,rgba(240,170,60,.55),rgba(150,70,10,.25) 45%,transparent 75%)}
  .banner--sparkle .headline{left:0;width:460px;top:82px;text-align:center;color:#fff}
  /* banner 3 */
  .gold-line{position:absolute;left:0;width:100%;height:5px;
    background:linear-gradient(90deg,var(--gold-dark),var(--gold-light),var(--gold),var(--gold-dark))}
  .banner--badge .gold-line{top:200px}
  .badge{position:absolute;left:96px;top:24px;width:200px;height:190px;border-radius:22px 22px 60px 60px;
    background:linear-gradient(160deg,var(--gold-light),#f6ecc8 40%,var(--gold))}
  .badge .headline{position:static;color:#444;font-size:26px;line-height:1.25;text-align:center;padding-top:22px}
  .badge-band{position:absolute;left:64px;top:192px;width:264px;height:40px;background:var(--red);
    color:#fff;font-size:19px;font-weight:600;letter-spacing:2px;text-align:center;line-height:40px}
  /* banner 4 */
  .banner--gold-bow .gold-line{top:38px;height:10px}
  .bow{position:absolute;left:44px;top:6px;width:110px;height:90px;border-radius:40%;
    background:radial-gradient(circle,var(--gold-light),var(--gold) 50%,var(--gold-dark))}
  .banner--gold-bow .headline{left:0;width:460px;top:110px;text-align:center;color:var(--blue);font-size:31px;line-height:1.22;font-weight:400}
  .banner--gold-bow .headline strong{color:#fff;font-weight:600}
</style>
</head>
<body>
  <section class="banner banner--ribbon">
    <div class="silk-ribbon" role="img" aria-label="Black satin ribbon with a bow and pearl centre"></div>
    <p class="headline">We are <em>CELEBRATING</em> our<br>10th Anniversary</p>
    <div class="mascot-panel"><div class="mascot" role="img" aria-label="Silver robot mascot waving"></div></div>
  </section>

  <section class="banner banner--sparkle">
    <div class="sparkle-waves" role="img" aria-label="Glowing golden light waves with sparkles"></div>
    <p class="headline">We are <em>CELEBRATING</em><br>our 10th Anniversary</p>
    <div class="mascot-panel"><div class="mascot" role="img" aria-label="Silver robot mascot waving"></div></div>
    <span class="brand">BRINDLECOVE</span>
  </section>

  <section class="banner banner--badge">
    <div class="gold-line"></div>
    <div class="mascot-panel" style="top:0"><div class="mascot" role="img" aria-label="Silver robot mascot waving"></div></div>
    <div class="badge"><p class="headline">We are<br><em>CELEBRATING</em><br>our 10th<br>Anniversary</p></div>
    <div class="badge-band">BRINDLECOVE</div>
  </section>

  <section class="banner banner--gold-bow">
    <div class="gold-line"></div>
    <div class="bow" role="img" aria-label="Gold ribbon bow"></div>
    <p class="headline">We are CELEBRATING<br>our 10th Anniversary<br><strong>and your text here</strong></p>
    <div class="mascot-panel" style="top:52px;height:218px"><div class="mascot" role="img" aria-label="Silver robot mascot waving" style="top:6px;height:180px;width:170px"></div></div>
    <span class="brand">BRINDLECOVE</span>
  </section>
</body>
</html>
```